One slide graphic for website

I am designing a series of sliders for my website http://new.kelmarbyte.com

The slide I am trying to create has the following message:

EVERY company is a media company.
Empower yours now!

Learn More >

The ideas I have had for imagery are an office building with the letters 'Every Company is a Media Company' either shone onto the building or letters on the building roof ledge ect.

Aby ideas you may have to improve on this would be appreciated.

The idea behind the slide is to promote a software application which gives marketing professionals the chance to increase their media coverage. The message also encourages companies to create their own news on a number of platforms as the media landscape has changed so much. Look at the blue finch stunt whereby they generated 10 million views on viddlo using PR alone.

Good luck and I look forward to seeing your ideas.

Marcus

```html
<!DOCTYPE html>
<html lang="en">
<head>
<meta charset="utf-8">
<title>Kelmarbyte – Every Company is a Media Company</title>
<link rel="stylesheet" href="https://fonts.googleapis.com/css2?family=Montserrat:wght@800;900&family=Open+Sans:ital,wght@0,400;0,700;1,300&display=swap">
<style>
  :root {
    --green: #1f8a3c;
    --green-dark: #166b2d;
    --green-light: #2ea04b;
    --orange: #f7941d;
    --purple: #7b3fa0;
    --ink: #111111;
    --grey: #8a8a8a;
    --grey-text: #555555;
    --white: #ffffff;
  }
  * { margin: 0; padding: 0; box-sizing: border-box; }
  html, body { width: 1200px; height: 564px; overflow: hidden; background: var(--white); }
  body { font-family: "Open Sans", Arial, sans-serif; position: relative; }

  .site-header { position: absolute; top: 0; left: 0; width: 1200px; height: 105px; background: var(--white); }
  .brand { position: absolute; left: 172px; top: 32px; font-size: 36px; font-weight: 400; color: var(--green); letter-spacing: 0.5px; }
  .contact-phone { position: absolute; left: 750px; top: 17px; font-size: 17px; color: var(--grey); }
  .social { position: absolute; left: 932px; top: 19px; display: flex; gap: 7px; }
  .social span { width: 20px; height: 20px; border-radius: 50%; background: #4a4a4a; display: block; }
  .header-actions { position: absolute; left: 794px; top: 49px; display: flex; gap: 5px; }
  .pill-btn { height: 26px; border-radius: 6px; color: var(--white); font-weight: 700; font-style: italic; font-size: 14px; display: flex; align-items: center; gap: 6px; padding: 0 12px 0 4px; text-transform: uppercase; }
  .pill-btn .dot { width: 18px; height: 18px; border-radius: 50%; background: var(--white); display: flex; align-items: center; justify-content: center; }
  .pill-btn--demo { background: var(--purple); width: 118px; }
  .pill-btn--login { background: var(--orange); width: 81px; }

  .main-nav { position: absolute; top: 105px; left: 0; width: 1200px; height: 44px; background: linear-gradient(var(--green-light), var(--green) 40%, var(--green-dark)); }
  .main-nav ul { list-style: none; position: absolute; left: 173px; top: 0; height: 44px; display: flex; }
  .main-nav li { height: 44px; display: flex; align-items: center; padding: 0 12px; color: var(--white); font-size: 12px; font-weight: 700; text-transform: uppercase; border-right: 1px solid rgba(0,0,0,0.18); }
  .main-nav li.is-active { background: var(--orange); padding: 0 14px; }

  .hero { position: absolute; top: 149px; left: 0; width: 1200px; height: 385px; overflow: hidden; }
  .hero-photo { position: absolute; inset: 0; background: linear-gradient(180deg, #9c9c9c 0%, #d2d2d2 30%, #a8a8a8 55%, #5e5e5e 100%); }
  .hero-headline { position: absolute; left: 202px; top: 82px; font-family: "Montserrat", Arial, sans-serif; font-weight: 900; text-transform: uppercase; font-size: 84px; line-height: 74px; letter-spacing: -6px; color: var(--ink); text-shadow: 2px 2px 0 rgba(255,255,255,0.35); }
  .hero-headline .accent { color: var(--orange); text-shadow: 2px 2px 0 #3a2a10; }
  .hero-cta { position: absolute; left: 448px; top: 273px; display: flex; align-items: center; gap: 14px; }
  .hero-cta .tagline { font-size: 12px; font-weight: 700; color: var(--ink); }
  .learn-btn { width: 154px; height: 36px; border-radius: 18px; background: var(--orange); display: flex; align-items: center; gap: 14px; padding-left: 6px; color: var(--white); font-family: "Montserrat", Arial, sans-serif; font-weight: 800; font-size: 15px; text-transform: uppercase; }
  .learn-btn .dot { width: 26px; height: 26px; border-radius: 50%; background: var(--white); display: flex; align-items: center; justify-content: center; }

  .intro-line { position: absolute; left: 232px; top: 540px; font-size: 28px; font-weight: 300; font-style: italic; color: var(--grey-text); white-space: nowrap; }
</style>
</head>
<body>
  <header class="site-header">
    <div class="brand">KELMARBYTE</div>
    <div class="contact-phone">t. +44 (0)1632 960418</div>
    <div class="social" aria-label="Social links"><span></span><span></span><span></span></div>
    <div class="header-actions">
      <div class="pill-btn pill-btn--demo"><span class="dot"><svg width="10" height="10" viewBox="0 0 10 10"><path d="M1 5h7M5 2l3 3-3 3" stroke="#7b3fa0" stroke-width="1.8" fill="none"/></svg></span>Free Demo</div>
      <div class="pill-btn pill-btn--login"><span class="dot"><svg width="10" height="10" viewBox="0 0 10 10"><path d="M1 5h7M5 2l3 3-3 3" stroke="#f7941d" stroke-width="1.8" fill="none"/></svg></span>Login</div>
    </div>
  </header>

  <nav class="main-nav">
    <ul>
      <li class="is-active">Home</li>
      <li>Software</li>
      <li>Industries</li>
      <li>News</li>
      <li>Webinars</li>
      <li>Free Downloads</li>
      <li>Our Story</li>
      <li>Our Values</li>
      <li>Contact Us</li>
    </ul>
  </nav>

  <section class="hero">
    <div class="hero-photo" role="img" aria-label="Black and white photograph of a dense city skyline of office towers under a cloudy sky"></div>
    <h1 class="hero-headline">
      <span class="accent">Every</span>Company<br>
      <span class="accent">Is</span>A<span class="accent">Media</span>Company
    </h1>
    <div class="hero-cta">
      <span class="tagline">Empower yours now!</span>
      <div class="learn-btn"><span class="dot"><svg width="14" height="14" viewBox="0 0 14 14"><path d="M2 7h9M7 3l4 4-4 4" stroke="#f7941d" stroke-width="2.4" fill="none"/></svg></span>Learn More</div>
    </div>
  </section>

  <p class="intro-line">Fast and easy way to send press releases, manage your</p>
</body>
</html>
```